Lumen Wire Outlet - bag design for fiber optic cables

We need a packaging design for a clear ziplock bag that is 7" wide and 10" high. The design will be for a new line of fiber optic cable products. You can see the products on lumenwireoutlet.example. We would like to see designs that represent a superior quality product and an American brand. We want the equivalent of a nice retail bag that you would find in a store like Tech Haven. It should be a maximum of three colors. We really want something sharp, professional and eye catching, not whimsical or cartoonish. I've included a couple of examples below. I don't really like the designs attached but it will give you an idea. Please keep in mind the bag will be clear, not white.

Target Market(s)

Men 25-65

Industry/Entity Type

Optic

Colors

Designer to choose colors to be used in the design.

Requirements
Must have
• A clean design, not overly cluttered. These cables will be selling internationally so we need to show off the fact that we're an American brand. With that said, I don't want red, white and blue and over- the- top American. I would like something more subtle, classy that still says we are a USA brand. The bag should also incorporate the logo, which is attached. Please make it 3 colors maximum.
Nice to have
• clean, professional. The design doesn't need to have the colors in the logo. I'm open to any new colors introduced.
Should not have
• whimsical, colorful

```html
<!DOCTYPE html>
<html lang="en">
<head>
<meta charset="utf-8">
<title>Lumen Wire Outlet – Fiber Optic Patch Cable Bag</title>
<link rel="stylesheet" href="https://fonts.googleapis.com/css2?family=Questrial&family=Michroma&family=Oswald:wght@500&display=swap">
<style>
  :root {
    --backdrop: #a9a9a9;
    --bag-clear: #e4e4e6;
    --header-white: #f2f2f3;
    --plum-dark: #3b1630;
    --magenta: #b0127c;
    --magenta-bright: #e23ab6;
    --text-light: #ffffff;
    --text-dark: #3a3a3c;
    --brand-green: #4c8a2a;
  }
  * { margin: 0; padding: 0; box-sizing: border-box; }
  html, body { width: 1200px; height: 791px; overflow: hidden; }
  body {
    background: radial-gradient(ellipse at 50% 40%, #d4d4d4 0%, var(--backdrop) 75%);
    position: relative;
  }
  .bag {
    position: absolute;
    left: 390px; top: 80px;
    width: 420px; height: 630px;
    border-radius: 8px;
    overflow: hidden;
    background: var(--bag-clear);
    box-shadow: 0 20px 40px rgba(0,0,0,.25);
  }
  .bag-header {
    position: absolute; inset: 0 0 auto 0; height: 100px;
    background: var(--header-white);
  }
  .header-corner { position: absolute; top: 0; right: 0; }
  .hang-hole {
    position: absolute; top: 16px; left: 50%;
    width: 16px; height: 16px; margin-left: -8px;
    border-radius: 50%; background: var(--backdrop);
    border: 2px solid #c9c9cc;
  }
  .brand-name {
    position: absolute; left: 28px; top: 30px;
    display: flex; align-items: center; gap: 8px;
    font-family: "Questrial", sans-serif; font-size: 16px;
    color: var(--brand-green); line-height: 1.05;
  }
  .brand-name .dot { width: 12px; height: 12px; border-radius: 50%; background: var(--brand-green); }
  .zip-line {
    position: absolute; left: 0; right: 0; top: 100px; height: 6px;
    background: linear-gradient(#d0d0d3, #f5f5f6);
  }
  .color-band {
    position: absolute; left: 0; right: 0; top: 106px; height: 260px;
    background: linear-gradient(180deg, var(--magenta) 0%, #9c1870 45%, var(--magenta-bright) 58%, rgba(226,58,182,.35) 75%, rgba(228,228,230,0) 100%);
  }
  .connector-art {
    position: absolute; right: 0; top: 40px; width: 150px; height: 170px;
    background: linear-gradient(135deg, #e9ecea 0%, #b9bfbc 55%, #8fd0c6 100%);
    border-radius: 6px 0 0 40px; opacity: .9;
  }
  .product-title {
    position: absolute; left: 26px; top: 128px;
    font-family: "Questrial", sans-serif; font-size: 17px; line-height: 1.35;
    color: var(--text-light); letter-spacing: .3px;
  }
  .spec-badges { position: absolute; left: 28px; top: 188px; display: flex; gap: 8px; }
  .badge {
    border: 1.5px solid var(--text-light); border-radius: 4px;
    padding: 2px 5px; height: 30px;
    font-family: "Oswald", sans-serif; color: var(--text-light);
    display: flex; flex-direction: column; justify-content: center; align-items: center;
    line-height: 1;
  }
  .badge .big { font-size: 16px; }
  .badge .small { font-size: 6px; letter-spacing: .3px; }
  .badge .mid { font-size: 8px; }
  .pocket {
    position: absolute; left: 40px; right: 40px;
    border: 1px solid rgba(255,255,255,.7); border-radius: 14px;
    background: linear-gradient(180deg, rgba(255,255,255,.35), rgba(255,255,255,.08));
  }
  .pocket-upper { top: 300px; height: 140px; }
  .pocket-lower { top: 455px; height: 150px; }
  .product-type {
    position: absolute; left: 0; right: 0; bottom: 42px; text-align: center;
    font-family: "Michroma", sans-serif; color: var(--text-dark); line-height: 1;
  }
  .product-type .line-1 { font-size: 22px; letter-spacing: 1px; }
  .product-type .line-2 { font-size: 15px; letter-spacing: 2px; margin-top: 2px; }
</style>
</head>
<body>
  <div class="bag">
    <div class="bag-header">
      <svg class="header-corner" width="210" height="100" viewBox="0 0 210 100">
        <polygon points="40,0 210,0 210,100 0,100" fill="var(--plum-dark)"/>
      </svg>
      <div class="brand-name"><span class="dot"></span><span>Lumen Wire<br>Outlet</span></div>
      <div class="hang-hole"></div>
    </div>
    <div class="zip-line"></div>
    <div class="color-band"></div>
    <div class="connector-art" role="img" aria-label="Photo of LC duplex fiber optic connectors"></div>
    <div class="product-title">Plenum OM3 Multimode<br>Fiber Optic Patch Cable</div>
    <div class="spec-badges">
      <div class="badge"><span class="big">10<small style="font-size:7px">GB</small></span><span class="small">PER SEC</span></div>
      <div class="badge"><span class="big">LC</span><span class="small">TO LC</span></div>
      <div class="badge"><span class="big">7<small style="font-size:9px">MTR</small></span></div>
      <div class="badge"><span class="mid">LIFETIME</span><span class="small">WARRANTY</span></div>
    </div>
    <div class="pocket pocket-upper"></div>
    <div class="pocket pocket-lower"></div>
    <div class="product-type"><div class="line-1">FIBER</div><div class="line-2">OPTIC CABLE</div></div>
  </div>
</body>
</html>
```